Wren & Dory Pear Knoll - Promotion E-Mail

Email blast promoting a special week of discounts at our main campus. Purpose of the email is to notify our customers of this and entice them to come up to our campus to take advantage of the sales.

Details:

Our Biggest Fall Promotion Of The Year!
Join Us At Pear Knoll For Exciting Savings This Week Only!
It's Not Too Late To Visit Our Campus And Save

Special Savings From 10/24 - 10/30

* 40% Off All Apple Picking! Reduced To $1.00 Per Lb.!
* 20% Off Full Cases Of 1887 Bold Perry
*20% Off Wren & Dory Fudge
* 20% Off Gallons Of Wren & Dory Apple Cider
* Special Cocktail Savings

Fall Is Still In Full Swing And We Cannot Wait To See You On The Hill!

```html
<!DOCTYPE html>
<html lang="en">
<head>
<meta charset="utf-8">
<title>Wren &amp; Dory Pear Knoll – Fall Promotion</title>
<link href="https://fonts.googleapis.com/css2?family=Poppins:wght@400;500;600&family=Bodoni+Moda:ital,wght@0,400;1,400&display=swap" rel="stylesheet">
<style>
  :root {
    --sky: #b9cdd3;
    --orchard-light: #8aa06f;
    --orchard-dark: #3f5a2a;
    --grass: #6f8f3c;
    --panel: #ffffff;
    --rule: #e0606a;
    --ink: #111111;
    --fruit-core: #d9323c;
    --fruit-soft: #ec8c90;
    --band: rgba(255,255,255,0.9);
    --badge: #111111;
    --on-dark: #ffffff;
  }
  * { box-sizing: border-box; margin: 0; padding: 0; }
  html, body { width: 1029px; height: 1200px; overflow: hidden; }
  body { position: relative; font-family: "Poppins", sans-serif; color: var(--ink); }

  .orchard-backdrop {
    position: absolute; inset: 0;
    background: linear-gradient(180deg, var(--sky) 0%, #a9bcb6 22%, var(--orchard-light) 45%, var(--orchard-dark) 75%, var(--grass) 100%);
  }

  .promo-panel {
    position: absolute; left: 86px; top: 69px; width: 857px; height: 1063px;
    background: var(--panel);
  }
  .promo-frame {
    position: absolute; left: 24px; top: 20px; width: 808px; height: 1026px;
    border: 2px solid var(--rule);
  }

  .headline {
    position: absolute; top: 88px; left: 0; right: 0; text-align: center;
    font-weight: 600; font-size: 28px; letter-spacing: 0.2px;
  }
  .intro {
    position: absolute; top: 146px; left: 0; right: 0; text-align: center;
    font-size: 19px; line-height: 37px; font-weight: 400;
  }

  .fruit-visual {
    position: absolute; left: 248px; top: 262px; width: 370px; height: 457px;
    background: radial-gradient(ellipse 50% 50% at 50% 52%, var(--fruit-core) 0%, var(--fruit-soft) 62%, rgba(255,255,255,0) 100%);
  }
  .discount-band {
    position: absolute; left: 129px; top: 368px; width: 437px; height: 232px;
    background: var(--band);
  }
  .discount { font-family: "Bodoni Moda", serif; }
  .discount-upto {
    position: absolute; left: 171px; top: 386px;
    font-style: italic; font-size: 30px; line-height: 1; letter-spacing: 4px;
  }
  .discount-value {
    position: absolute; left: 209px; top: 353px;
    font-size: 250px; line-height: 1; font-weight: 400; letter-spacing: -14px;
  }
  .discount-off {
    position: absolute; left: 574px; top: 555px;
    font-style: italic; font-size: 46px; line-height: 1; letter-spacing: 3px;
  }

  .savings-title {
    position: absolute; top: 744px; left: 0; right: 0; text-align: center;
    font-weight: 500; font-size: 33px;
  }
  .savings-dates {
    position: absolute; top: 794px; left: 319px; width: 219px; height: 32px;
    background: var(--badge); color: var(--on-dark);
    font-weight: 600; font-size: 18px; line-height: 32px; text-align: center;
  }
  .savings-list {
    position: absolute; top: 849px; left: 0; right: 0; list-style: none;
    text-align: center; font-size: 19px; line-height: 31px;
  }

  .signoff {
    position: absolute; top: 1147px; left: 0; right: 0; text-align: center;
    color: var(--on-dark); font-weight: 500; font-size: 18.5px;
  }
</style>
</head>
<body>
  <div class="orchard-backdrop" role="img" aria-label="Apple orchard rows under a pale sky"></div>

  <main class="promo-panel">
    <div class="promo-frame"></div>

    <h1 class="headline">Our Biggest Fall Promotion Of The Year!</h1>
    <p class="intro">Join Us At Pear Knoll For Exciting Savings This Week Only!<br>It's Not Too Late To Visit Our Campus And Save</p>

    <div class="fruit-visual" role="img" aria-label="Photo of a single red apple"></div>
    <div class="discount-band"></div>
    <div class="discount">
      <span class="discount-upto">UPTO</span>
      <span class="discount-value">40%</span>
      <span class="discount-off">OFF</span>
    </div>

    <h2 class="savings-title">Special Savings</h2>
    <div class="savings-dates">From 10/24 - 10/30</div>
    <ul class="savings-list">
      <li>40% Off All Apple Picking! Reduced To $1.00 Per Lb.!</li>
      <li>20% Off Full Cases Of 1887 Bold Perry</li>
      <li>20% Off Wren &amp; Dory Fudge</li>
      <li>20% Off Gallons Of Wren &amp; Dory Apple Cider</li>
      <li>Special Cocktail Savings</li>
    </ul>
  </main>

  <p class="signoff">Fall Is Still In Full Swing And We Cannot Wait To See You On The Hill!</p>
</body>
</html>
```